business card for a shoe shop

we would like a business card for a family owned shoe shop.
With this information included.
Darnell's Shoe Store
Family owned since 1947

then on other side
Darnell's Shoe Store
Footwear fitting specialist
Phone: 9187 2630
218 Quarry St, Fernleigh Downs 3187
(cnr. Hartwick Rd and Quarry St)
darnellshoes218@examplemail.com
if could incorporate the purple color on card i have attached.

```html
<!DOCTYPE html>
<html lang="en">
<head>
<meta charset="utf-8">
<title>Darnell's Shoe Store – Business Card</title>
<link rel="stylesheet" href="https://fonts.googleapis.com/css2?family=Montserrat:wght@800&family=Poppins:wght@400;600&display=swap">
<style>
  :root {
    --purple: #7f3ff0;
    --ink: #111111;
    --card-white: #f8f8f8;
    --card-black: #000000;
    --faint: #e9e9e9;
    --backdrop: #e4e1df;
    --on-dark: #ffffff;
  }
  * { box-sizing: border-box; margin: 0; padding: 0; }
  html, body { width: 1200px; height: 1181px; overflow: hidden; }
  body {
    background: var(--backdrop);
    font-family: "Poppins", sans-serif;
    position: relative;
  }
  .card {
    position: absolute;
    width: 654px;
    height: 403px;
    overflow: hidden;
    text-align: center;
  }
  .card--front { left: 179px; top: 166px; background: var(--card-white); color: var(--ink); }
  .card--back { left: 475px; top: 627px; background: var(--card-black); color: var(--on-dark); }

  .bg-ring {
    position: absolute;
    left: 490px; top: 0;
    width: 324px; height: 324px;
    border: 12px solid var(--faint);
    border-radius: 50%;
  }
  .brand-ring {
    position: absolute;
    left: 50%;
    border: 4px solid var(--purple);
    border-radius: 50%;
    transform: translateX(-50%);
  }
  .card--front .brand-ring { top: 22px; width: 76px; height: 76px; }
  .card--back .brand-ring { top: 66px; width: 120px; height: 120px; }
  .brand-name {
    position: absolute;
    left: 0; right: 0;
    color: var(--purple);
    font-weight: 600;
    line-height: 1;
  }
  .card--front .brand-name { top: 110px; font-size: 20px; }
  .card--back .brand-name { top: 210px; font-size: 38px; }

  .tagline-title {
    position: absolute;
    left: 0; right: 0; top: 154px;
    font-family: "Montserrat", sans-serif;
    font-weight: 800;
    font-size: 23px;
    line-height: 29px;
  }
  .tagline-title span { display: block; letter-spacing: 9px; padding-left: 9px; }

  .contact {
    position: absolute;
    left: 0; right: 0; top: 244px;
    font-size: 19px;
    line-height: 24px;
  }
  .contact-line { display: flex; justify-content: center; align-items: center; gap: 6px; }
  .contact-line svg { fill: var(--purple); flex: none; }
  .address {
    position: absolute;
    left: 0; right: 0; top: 325px;
    font-size: 19px;
    line-height: 24px;
  }
  .since {
    position: absolute;
    left: 0; right: 0; top: 322px;
    font-size: 19px;
  }
</style>
</head>
<body>
  <section class="card card--front" aria-label="Business card front">
    <div class="bg-ring" aria-hidden="true"></div>
    <div class="brand-ring" aria-hidden="true"></div>
    <p class="brand-name">Darnell's Shoe Store</p>
    <h1 class="tagline-title">Footwear Fitting<span>Specialist</span></h1>
    <div class="contact">
      <p class="contact-line">
        <svg width="16" height="14" viewBox="0 0 16 14" aria-hidden="true"><path d="M1 4c0-2 3-3 7-3s7 1 7 3v1h-3V3.5C11 3 9.5 2.8 8 2.8S5 3 4 3.5V5H1zM4 6h8l2 7H2z"/></svg>
        9187 2630
      </p>
      <p class="contact-line">
        <svg width="16" height="12" viewBox="0 0 16 12" aria-hidden="true"><path d="M0 0h16v12H0zM1.5 1.5 8 7l6.5-5.5v-.2h-13z" fill-rule="evenodd"/></svg>
        darnellshoes218@examplemail.com
      </p>
    </div>
    <p class="address">218 Quarry St, Fernleigh Downs 3187<br>(cnr. Hartwick Rd and Quarry St)</p>
  </section>

  <section class="card card--back" aria-label="Business card back">
    <div class="brand-ring" aria-hidden="true"></div>
    <p class="brand-name">Darnell's Shoe Store</p>
    <p class="since">Family owned since 1947</p>
  </section>
</body>
</html>
```